SEO Friendly Web Design Needed for Leading Software Company

Founded in 1986, TRVQ is the market leader for innovative software solutions for the heavy civil construction industry. Our suite of products, including the bestsellers GirderQuote® and SiteLedger®, are used by more than 40,000 workers every day to improve their proficiency at estimating, job management, resource management, safety and equipment maintenance. TRVQ also offers new mobile applications and cloud computing services so companies can work on a wide array of devices including laptops, tablets and smartphones.

In addition to high quality software, TRVQ is best known for providing world-class customer service, and for its friendly, employee-ownership culture. We offer a full range of professional support options to help customers maximize their software investment including implementation planning, training and INSTANT 24/7 phone support.

Goals, objectives and target audience

The goal of our new layout and design will be to increase conversions, enhance user experience and enhance our SERP rankings.

Our objectives are as follows:
1. Clean and well laid out home page. White space is OK.
2. CTAs in strategic locations throughout to drive conversions and MQLs
3. SEO rich content with appropriate layout to meet our SEO requirements
4. 2 Master Design Templates – Home & Internal
5. Custom Design elements for individual modules

Target Audience:
- Heavy / Civil Construction Industry
- C Level executives or persons in leadership roles who utilize our software
- MEN in the construction industry.

Requirements
Should not have
• Feminine design - our industry is largely male construction workers.
Don't use script or goofy fonts
Don't change the logo, or put it in an image where it is not easily viewable.

```html
<!DOCTYPE html>
<html lang="en">
<head>
<meta charset="utf-8">
<title>TRVQ – Software Overview</title>
<link rel="stylesheet" href="https://fonts.googleapis.com/css2?family=Open+Sans:wght@400;600;700&display=swap">
<style>
:root{
  --green:#06683a;
  --orange:#f7931e;
  --dark:#2a2a2a;
  --ink:#222;
  --muted:#777;
  --rule:#d6d6d6;
  --band:#efefef;
  --white:#fff;
}
*{box-sizing:border-box;margin:0;padding:0}
html,body{width:1200px;height:3724px;overflow:hidden}
body{font-family:"Open Sans",Arial,sans-serif;color:var(--ink);background:var(--white);position:relative}
a{color:inherit;text-decoration:none}
ul{list-style:none}

.topbar{height:34px;background:var(--dark);color:#ddd;font-size:12px;display:flex;justify-content:space-between;align-items:center;padding:0 157px}
.topbar .accent{color:var(--orange)}

.site-header{height:130px;display:flex;align-items:center;justify-content:space-between;padding:0 157px;border-bottom:1px solid var(--rule)}
.brand{display:flex;align-items:center;gap:12px;font-weight:700;font-size:30px;color:var(--green);letter-spacing:1px}
.brand .mark{width:34px;height:34px;background:var(--orange)}
.main-nav{display:flex;gap:30px;font-size:14px;color:#888}

.page-title{height:86px;background:var(--band);display:flex;align-items:center;justify-content:center;font-size:32px;font-weight:400}
.page-title span{color:var(--orange)}

.overview{height:370px;position:relative;padding:20px 157px}
.overview h1{font-size:38px;font-weight:400;width:490px;padding-bottom:10px;border-bottom:1px solid var(--rule)}
.overview .lede{font-size:13px;color:var(--muted);margin:14px 0 12px}
.benefits li{display:flex;align-items:center;gap:8px;font-size:13px;line-height:24px;color:#444}
.benefits svg{width:14px;height:14px}
.btn{display:inline-flex;align-items:center;justify-content:center;width:130px;height:32px;background:var(--orange);color:#fff;font-size:13px;font-weight:600}
.overview .actions{display:flex;gap:130px;margin-top:26px}
.tile-grid{position:absolute;left:695px;top:15px;display:grid;grid-template-columns:repeat(3,90px);gap:20px}
.tile{width:90px;height:90px;background:var(--green);border:2px solid #0c4a2a;display:flex;align-items:center;justify-content:center}
.tile svg{width:52px;height:52px}

.module{height:330px;position:relative;padding:22px 157px 0;border-top:1px solid var(--rule);box-shadow:inset 0 8px 10px -8px rgba(0,0,0,.12)}
.module h2{font-size:28px;font-weight:400;line-height:32px;height:68px;width:220px}
.module .icon-box{position:absolute;left:157px;top:100px;width:208px;height:208px;background:var(--green);display:flex;align-items:center;justify-content:center}
.module .icon-box svg{width:110px;height:110px}
.module .body{position:absolute;left:385px;top:100px;width:560px}
.module .body p{font-size:13px;color:#444;margin-bottom:8px}
.module .actions{display:flex;gap:130px;margin:34px 0 0 18px}
.back-top{position:absolute;left:850px;top:294px;font-size:11px;color:#aaa;display:flex;align-items:center;gap:4px}

.cta-band{height:85px;background:var(--dark);display:flex;align-items:center;justify-content:space-between;padding:0 330px 0 157px;color:#eee;font-size:22px}
.cta-band .btn{width:90px}

.site-footer{height:379px;background:var(--band);padding:48px 157px 0;display:grid;grid-template-columns:140px 140px 140px 150px 200px 120px;gap:16px}
.site-footer h3{font-size:20px;font-weight:400;margin-bottom:14px}
.site-footer li{font-size:12px;line-height:20px;color:var(--orange)}
.site-footer .contact li{color:#444}
.site-footer .contact b{font-weight:700}
.social{display:grid;grid-template-columns:22px;gap:10px}
.social span{width:22px;height:22px;background:#9a9a9a;display:block}
</style>
</head>
<body>
<svg width="0" height="0" style="position:absolute">
  <defs>
    <symbol id="i-list" viewBox="0 0 60 60"><rect x="8" y="6" width="44" height="48" fill="none" stroke="#111" stroke-width="3"/><g stroke="#111" stroke-width="5"><line x1="14" y1="16" x2="46" y2="16"/><line x1="14" y1="26" x2="46" y2="26"/><line x1="14" y1="36" x2="46" y2="36"/><line x1="14" y1="46" x2="46" y2="46"/></g></symbol>
    <symbol id="i-swap" viewBox="0 0 60 60"><g fill="none" stroke="#111" stroke-width="3"><path d="M6 22h40l-8-8M54 38H14l8 8"/><path d="M46 22 28 42"/></g></symbol>
    <symbol id="i-route" viewBox="0 0 60 60"><g fill="none" stroke="#111" stroke-width="3"><path d="M4 30h50M40 16l14 14-14 14"/><path d="M4 14c14 0 20 16 30 16M4 46c14 0 20-16 30-16"/></g></symbol>
    <symbol id="i-lock" viewBox="0 0 60 60"><path d="M18 26v-8a12 12 0 0 1 24 0v8" fill="none" stroke="#111" stroke-width="5"/><rect x="12" y="26" width="36" height="28" rx="2" fill="#111"/></symbol>
    <symbol id="i-pin" viewBox="0 0 60 60"><path d="M30 4a16 16 0 0 0-16 16c0 14 16 36 16 36s16-22 16-36A16 16 0 0 0 30 4z" fill="#111"/><circle cx="30" cy="20" r="6" fill="#06683a"/></symbol>
    <symbol id="i-gear" viewBox="0 0 60 60"><g fill="#111"><circle cx="30" cy="30" r="16"/><g stroke="#111" stroke-width="8"><line x1="30" y1="6" x2="30" y2="54"/><line x1="6" y1="30" x2="54" y2="30"/><line x1="13" y1="13" x2="47" y2="47"/><line x1="47" y1="13" x2="13" y2="47"/></g></g><circle cx="30" cy="30" r="7" fill="#06683a"/></symbol>
    <symbol id="i-phone" viewBox="0 0 60 60"><rect x="17" y="4" width="26" height="52" rx="4" fill="none" stroke="#111" stroke-width="3"/><rect x="21" y="11" width="18" height="34" fill="none" stroke="#111" stroke-width="2"/><circle cx="30" cy="50" r="2.5" fill="#111"/></symbol>
    <symbol id="i-fuel" viewBox="0 0 60 60"><rect x="10" y="8" width="26" height="46" rx="2" fill="#111"/><rect x="15" y="13" width="16" height="12" fill="#06683a"/><path d="M36 20h6l6 8v18a3 3 0 0 1-6 0V34h-6" fill="none" stroke="#111" stroke-width="3"/></symbol>
    <symbol id="i-check" viewBox="0 0 14 14"><rect x="0.5" y="0.5" width="13" height="13" fill="#fff" stroke="#06683a"/><path d="M3 7l3 3 5-6" fill="none" stroke="#06683a" stroke-width="2"/></symbol>
    <symbol id="i-up" viewBox="0 0 10 10"><path d="M1 7l4-4 4 4" fill="none" stroke="#aaa" stroke-width="1.5"/></symbol>
  </defs>
</svg>

<div class="topbar">
  <span>Tools: <span class="accent">844-555-0142</span></span>
  <span>Contact Us: <span class="accent">Sales | Support</span></span>
</div>

<header class="site-header">
  <a class="brand" href="#"><span class="mark"></span>TRVQ</a>
  <nav class="main-nav">
    <a href="#">Software</a><a href="#">Services</a><a href="#">Pricing</a><a href="#">Who we are &amp; TRVQ</a><a href="#">Events</a><a href="#">About Us</a>
  </nav>
</header>

<div class="page-title">Software&nbsp;<span>Overview</span></div>

<section class="overview">
  <h1>Construction Software</h1>
  <p class="lede">TRVQ software description overview. Explain major reasons to use the suite.</p>
  <ul class="benefits">
    <li><svg><use href="#i-check"/></svg>Software Benefit</li>
    <li><svg><use href="#i-check"/></svg>Software Benefit</li>
    <li><svg><use href="#i-check"/></svg>Software Benefit</li>
    <li><svg><use href="#i-check"/></svg>Software Benefit</li>
    <li><svg><use href="#i-check"/></svg>Software Benefit</li>
  </ul>
  <div class="actions"><a class="btn" href="#">Contact Sales</a><a class="btn" href="#">Demo</a></div>
  <div class="tile-grid">
    <div class="tile"><svg><use href="#i-list"/></svg></div>
    <div class="tile"><svg><use href="#i-swap"/></svg></div>
    <div class="tile"><svg><use href="#i-route"/></svg></div>
    <div class="tile"><svg><use href="#i-list"/></svg></div>
    <div class="tile"><svg><use href="#i-swap"/></svg></div>
    <div class="tile"><svg><use href="#i-route"/></svg></div>
    <div class="tile"><svg><use href="#i-list"/></svg></div>
    <div class="tile"><svg><use href="#i-swap"/></svg></div>
    <div class="tile"><svg><use href="#i-route"/></svg></div>
  </div>
</section>

<section class="module">
  <h2>Estimating &amp; Bidding</h2>
  <div class="icon-box"><svg><use href="#i-list"/></svg></div>
  <div class="body">
    <p>Description of software offering and how it addresses need.</p>
    <ul class="benefits"><li><svg><use href="#i-check"/></svg>Main Software Benefit</li><li><svg><use href="#i-check"/></svg>Main Software Benefit</li><li><svg><use href="#i-check"/></svg>Main Software Benefit</li></ul>
    <div class="actions"><a class="btn" href="#">Contact Sales</a><a class="btn" href="#">Read More</a></div>
  </div>
  <a class="back-top" href="#"><svg width="10" height="10"><use href="#i-up"/></svg>Back to top</a>
</section>

<section class="module">
  <h2>Job Management</h2>
  <div class="icon-box"><svg><use href="#i-swap"/></svg></div>
  <div class="body">
    <p>Description of software offering and how it addresses need.</p>
    <ul class="benefits"><li><svg><use href="#i-check"/></svg>Main Software Benefit</li><li><svg><use href="#i-check"/></svg>Main Software Benefit</li><li><svg><use href="#i-check"/></svg>Main Software Benefit</li></ul>
    <div class="actions"><a class="btn" href="#">Contact Sales</a><a class="btn" href="#">Read More</a></div>
  </div>
  <a class="back-top" href="#"><svg width="10" height="10"><use href="#i-up"/></svg>Back to top</a>
</section>

<section class="module">
  <h2>Dispatching &amp; Scheduling</h2>
  <div class="icon-box"><svg><use href="#i-route"/></svg></div>
  <div class="body">
    <p>Description of software offering and how it addresses need.</p>
    <ul class="benefits"><li><svg><use href="#i-check"/></svg>Main Software Benefit</li><li><svg><use href="#i-check"/></svg>Main Software Benefit</li><li><svg><use href="#i-check"/></svg>Main Software Benefit</li></ul>
    <div class="actions"><a class="btn" href="#">Contact Sales</a><a class="btn" href="#">Read More</a></div>
  </div>
  <a class="back-top" href="#"><svg width="10" height="10"><use href="#i-up"/></svg>Back to top</a>
</section>

<section class="module">
  <h2>Safety Management</h2>
  <div class="icon-box"><svg><use href="#i-lock"/></svg></div>
  <div class="body">
    <p>Description of software offering and how it addresses need.</p>
    <ul class="benefits"><li><svg><use href="#i-check"/></svg>Main Software Benefit</li><li><svg><use href="#i-check"/></svg>Main Software Benefit</li><li><svg><use href="#i-check"/></svg>Main Software Benefit</li></ul>
    <div class="actions"><a class="btn" href="#">Contact Sales</a><a class="btn" href="#">Read More</a></div>
  </div>
  <a class="back-top" href="#"><svg width="10" height="10"><use href="#i-up"/></svg>Back to top</a>
</section>

<section class="module">
  <h2>GPS</h2>
  <div class="icon-box"><svg><use href="#i-pin"/></svg></div>
  <div class="body">
    <p>Description of software offering and how it addresses need.</p>
    <ul class="benefits"><li><svg><use href="#i-check"/></svg>Main Software Benefit</li><li><svg><use href="#i-check"/></svg>Main Software Benefit</li><li><svg><use href="#i-check"/></svg>Main Software Benefit</li></ul>
    <div class="actions"><a class="btn" href="#">Contact Sales</a><a class="btn" href="#">Read More</a></div>
  </div>
  <a class="back-top" href="#"><svg width="10" height="10"><use href="#i-up"/></svg>Back to top</a>
</section>

<section class="module">
  <h2>Equipment Maintenance</h2>
  <div class="icon-box"><svg><use href="#i-gear"/></svg></div>
  <div class="body">
    <p>Description of software offering and how it addresses need.</p>
    <ul class="benefits"><li><svg><use href="#i-check"/></svg>Main Software Benefit</li><li><svg><use href="#i-check"/></svg>Main Software Benefit</li><li><svg><use href="#i-check"/></svg>Main Software Benefit</li></ul>
    <div class="actions"><a class="btn" href="#">Contact Sales</a><a class="btn" href="#">Read More</a></div>
  </div>
  <a class="back-top" href="#"><svg width="10" height="10"><use href="#i-up"/></svg>Back to top</a>
</section>

<section class="module">
  <h2>Mobile Apps</h2>
  <div class="icon-box"><svg><use href="#i-phone"/></svg></div>
  <div class="body">
    <p>Description of software offering and how it addresses need.</p>
    <ul class="benefits"><li><svg><use href="#i-check"/></svg>Main Software Benefit</li><li><svg><use href="#i-check"/></svg>Main Software Benefit</li><li><svg><use href="#i-check"/></svg>Main Software Benefit</li></ul>
    <div class="actions"><a class="btn" href="#">Contact Sales</a><a class="btn" href="#">Read More</a></div>
  </div>
  <a class="back-top" href="#"><svg width="10" height="10"><use href="#i-up"/></svg>Back to top</a>
</section>

<section class="module">
  <h2>Fuel Tracking</h2>
  <div class="icon-box"><svg><use href="#i-fuel"/></svg></div>
  <div class="body">
    <p>Description of software offering and how it addresses need.</p>
    <ul class="benefits"><li><svg><use href="#i-check"/></svg>Main Software Benefit</li><li><svg><use href="#i-check"/></svg>Main Software Benefit</li><li><svg><use href="#i-check"/></svg>Main Software Benefit</li></ul>
    <div class="actions"><a class="btn" href="#">Contact Sales</a><a class="btn" href="#">Read More</a></div>
  </div>
  <a class="back-top" href="#"><svg width="10" height="10"><use href="#i-up"/></svg>Back to top</a>
</section>

<div class="cta-band">
  <span>Text highlighting feature overview with CTA</span>
  <a class="btn" href="#">CTA</a>
</div>

<footer class="site-footer">
  <div><h3>Software</h3><ul><li>GirderQuote®</li><li>SiteLedger®</li><li>Dispatcher</li><li>Safety</li><li>GPS</li><li>Equipment</li><li>Mobile Apps</li><li>Fuel Tracking</li></ul></div>
  <div><h3>Services</h3><ul><li>Consulting</li><li>Training</li><li>Support</li><li>Implementation</li><li>User Groups</li><li>Cloud Hosting</li></ul></div>
  <div><h3>News</h3><ul><li>Press Releases</li><li>Events</li><li>Newsletter</li><li>Webinars</li><li>Customer Stories</li></ul></div>
  <div><h3>About Us</h3><ul><li>Who We Are</li><li>Employee Ownership</li><li>Careers</li><li>Partners</li><li>Contact</li></ul></div>
  <div class="contact"><h3>TRVQ</h3><ul><li><b>Sales:</b> 844-555-0170</li><li><b>Support:</b> 844-555-0188</li><li><b>Email:</b> info@trvq-soft.com</li><li>4820 Quarry Ridge Rd</li><li>Halden, TX 77019</li></ul></div>
  <div><h3>Social</h3><div class="social"><span></span><span></span><span></span><span></span></div></div>
</footer>
</body>
</html>
```